"Trade with Tilda" needs a funky and stylish business card

Hi my name is Tilda, I am an experienced Bidnest Prime Vendor with a 100% satisfaction rating and over 400 items sold

My business name and bidnest username is "Trade with Tilda" I sell other peoples items on Bidnest for a commission. The main items I sell are furniture and renovation/building salvage items such as used kitchens, bathrooms , window doors etc.

I will be promoting my service in real estate agent offices, storage facilities, removalists, building and renovating companies.

i believe selling on bidnest is a great way for people to recycle their used goods and salvageable materials and reduce waste and landfill.

Target Market(s)

people selling their homes, renovators, builders, downsizers

Industry/Entity Type

Real Estate

Contact Information for Business Card

Tilda Marlowe
0492716045

Logo Text

Trade with Tilda

Logo styles of interest
Wordmark Logo
Requirements
Must have
• the business card must feature the bidnest logo mentioning primevendorr gold ranked vendor I have attached a copy
Nice to have
• i would like to have the trade with tilda logo written in royal blue

```html
<!DOCTYPE html>
<html lang="en">
<head>
<meta charset="utf-8">
<title>Tilda Marlowe – Business Card</title>
<link rel="stylesheet" href="https://fonts.googleapis.com/css2?family=Gelasio:wght@400;600&display=swap">
<style>
  :root {
    --card-grey: #bcc3c1;
    --side-blue-deep: #8f9bc6;
    --side-blue-pale: #d3d8da;
    --royal-blue: #1f3ff2;
    --lavender: #9ba7d8;
    --ink: #2a2b2c;
    --gold: #e9b320;
    --white: #ffffff;
  }
  html, body {
    margin: 0;
    padding: 0;
    width: 1200px;
    height: 694px;
    overflow: hidden;
    background: #ffffff;
  }
  .card {
    position: relative;
    width: 1200px;
    height: 694px;
    overflow: hidden;
    background: var(--card-grey);
    font-family: "Gelasio", Georgia, serif;
    color: var(--ink);
  }
  .card-art {
    position: absolute;
    inset: 0;
    width: 1200px;
    height: 694px;
  }
  .wordmark-name {
    font-family: "Gelasio", Georgia, serif;
    font-size: 74px;
    letter-spacing: 2px;
    fill: var(--ink);
  }
  .wordmark-lead {
    font-family: "Gelasio", Georgia, serif;
    font-size: 26px;
    font-weight: 600;
    letter-spacing: 1px;
    fill: var(--royal-blue);
  }
  .contact {
    position: absolute;
    top: 62px;
    right: 38px;
    text-align: right;
  }
  .contact-name,
  .contact-phone {
    margin: 0;
    font-size: 46px;
    line-height: 1.0;
    letter-spacing: 1px;
    font-weight: 400;
  }
  .contact-phone {
    margin-top: 30px;
    font-variant-numeric: oldstyle-nums;
  }
  .marketplace {
    position: absolute;
    right: 28px;
    bottom: 34px;
    text-align: right;
    color: var(--white);
  }
  .marketplace-name {
    display: block;
    font-size: 44px;
    font-weight: 600;
    line-height: 1;
  }
  .marketplace-tier {
    display: block;
    margin-top: 6px;
    font-size: 18px;
    font-weight: 600;
    letter-spacing: 1px;
  }
</style>
</head>
<body>
<main class="card">
  <svg class="card-art" viewBox="0 0 1061 614" preserveAspectRatio="none" aria-hidden="true">
    <defs>
      <linearGradient id="side-panel" x1="0" y1="1" x2="0.6" y2="0">
        <stop offset="0" stop-color="var(--side-blue-deep)"/>
        <stop offset="1" stop-color="var(--side-blue-pale)"/>
      </linearGradient>
      <filter id="paper-grain" x="0" y="0" width="100%" height="100%">
        <feTurbulence type="fractalNoise" baseFrequency="0.9" numOctaves="2" seed="4"/>
        <feColorMatrix type="matrix" values="0 0 0 0 0.5  0 0 0 0 0.52  0 0 0 0 0.52  0 0 0 0.18 0"/>
        <feComposite in2="SourceGraphic" operator="in"/>
      </filter>
    </defs>

    <rect class="paper" width="1061" height="614" fill="var(--card-grey)"/>
    <rect class="paper-grain" width="1061" height="614" fill="#000" filter="url(#paper-grain)"/>

    <path class="side-panel"
          d="M0 0 L242 0 C180 70 95 150 85 195 C78 225 120 228 170 232 C225 238 225 280 195 320 L80 614 L0 614 Z"
          fill="url(#side-panel)"/>

    <path class="curve-highlight"
          d="M85 205 C80 240 125 244 172 250 C212 256 214 282 192 315"
          fill="none" stroke="var(--white)" stroke-width="12" stroke-linecap="round" opacity="0.9"/>

    <path class="curve-line"
          d="M242 0 C180 70 95 150 85 195 C78 225 120 228 170 232 C225 238 225 280 195 320 L80 614"
          fill="none" stroke="var(--royal-blue)" stroke-width="10"/>

    <g class="wordmark" transform="translate(212 228) rotate(-56)">
      <text class="wordmark-name" x="0" y="0">TILDA</text>
      <text class="wordmark-lead" x="4" y="36">Trade with Tilda</text>
    </g>

    <path class="sweep-back" d="M1061 205 C960 390 820 525 630 614 L1061 614 Z" fill="var(--lavender)"/>
    <path class="sweep-front" d="M1061 240 C980 405 850 540 680 614 L1061 614 Z" fill="var(--royal-blue)"/>

    <circle class="rating-badge" cx="820" cy="535" r="36" fill="var(--gold)"/>
  </svg>

  <section class="contact">
    <h1 class="contact-name">Tilda Marlowe</h1>
    <p class="contact-phone">0492716045</p>
  </section>

  <div class="marketplace">
    <span class="marketplace-name">Bidnest</span>
    <span class="marketplace-tier">Prime Vendor</span>
  </div>
</main>
</body>
</html>
```